Design website for new email startup

We are starting a company called Posta.QZ (it will live at http://posta.qz.example).

We would like the main landing page for our site designed. We have provided a very simple wireframe to help provide direction for the content it should include, but we do not expect the designers to adhere to it at all - we encourage unique ideas. There is some sample text in the wireframe - this does not have to be used, but may provide ideas.

We provide an easy way for people to manage email for a custom domain name. For example if you own "myfamilyword.example" you can point your DNS records to us and we'll make it easy to have emails addressed to your domain get forwarded to your existing email (vexmail, etc). Folks running blogs, and other small sites can quickly setup email addresses for their domains and manage them in one place.

(For technical folks, we have you point your dns mx records to us, hence the name. That way all your email hits us and we can redirect it wherever you want. We make it easy to manage a single domain or a bunch of domains. Many domain registrars offer this service for a fee, and have clumsy management tools. We provide a robust simple toolset for free, as well as premium options).

The goal of the landing page is to get folks into the signup flow. The second priority flow is to have them take a look at the premium plan offerings.

We may offer the winning designer additional work for the remainder of the site design.
Updates

I've changed this project to a committed payment.  It is no longer refundable.  Thank you.

Target Market(s)

Bloggers, podcasters, designers, app developers - people who are a little tech savvy.

Industry/Entity Type

It Company

Font styles to use
Sans Serif

Colors

Designer to choose colors to be used in the design.

Requirements
Must have
• A full fidelity mockup (comp) of the landing page including the source file (psd, ai, etc).

Some sort of logo treatment for the posta.qz brand

A call to action for signup, such as the suggested 'Get Started Here'
Nice to have
• A hip startup feel

Incorporation of the email theme

Give the impression it is simple, easy and fast

```html
<!DOCTYPE html>
<html lang="en">
<head>
<meta charset="utf-8">
<title>Posta.QZ — Email for your domain</title>
<link href="https://fonts.googleapis.com/css2?family=Open+Sans:wght@400;600;700;800&family=Arimo:ital,wght@0,400;1,400&display=swap" rel="stylesheet">
<style>
:root{
  --ink:#222222;
  --text:#555555;
  --green:#5fa52a;
  --green-dark:#4b8d1c;
  --green-light:#78b93d;
  --white:#ffffff;
  --rule:#444444;
  --footer:#333333;
  --footer-text:#e6e6e6;
  --btn-gray:#6e6e6e;
  --yellow:#f5c400;
  --yellow-dark:#e6a800;
}
*{box-sizing:border-box;margin:0;padding:0}
html,body{width:1123px;height:1200px;overflow:hidden;background:var(--white)}
body{position:relative;font-family:"Arimo",Arial,sans-serif;color:var(--text)}

.site-header{position:absolute;left:0;top:0;width:1123px;height:112px;background:linear-gradient(#ffffff 70%,#ececec)}
.site-header::after{content:"";position:absolute;left:0;bottom:0;width:100%;height:6px;background:var(--rule)}
.brand{position:absolute;left:79px;top:26px;font-family:"Open Sans",sans-serif;font-weight:700;font-size:46px;letter-spacing:-0.5px;color:var(--ink)}
.main-nav{position:absolute;right:68px;top:75px;font-family:"Open Sans",sans-serif;font-size:14.5px;color:var(--ink)}
.main-nav a{color:inherit;text-decoration:none}
.main-nav .sep{margin:0 14px}

.hero{position:absolute;left:0;top:112px;width:1123px;height:416px;background:linear-gradient(100deg,var(--green-dark),var(--green) 45%,var(--green-light));box-shadow:0 3px 6px rgba(0,0,0,.25)}
.hero-photo{position:absolute;left:41px;top:39px;width:490px;height:332px;border-radius:10px;background:linear-gradient(160deg,#cfe3f2,#9ec6e6 45%,#f2f2f2);box-shadow:0 4px 10px rgba(0,0,0,.35);border:2px solid #fff}
.hero-points{position:absolute;left:592px;top:40px;width:470px;list-style:none;font-style:italic;font-size:22px;line-height:30px;color:var(--white)}
.hero-points li{position:relative;padding-left:22px;margin-bottom:16px}
.hero-points li::before{content:"";position:absolute;left:-6px;top:10px;width:12px;height:12px;border-radius:50%;background:var(--white)}
.hero-arrow{position:absolute;left:566px;top:283px}
.btn{position:absolute;display:flex;align-items:center;justify-content:center;font-family:"Open Sans",sans-serif;font-weight:800;font-size:19.5px;border-radius:26px;text-decoration:none}
.btn-start{left:633px;top:311px;width:214px;height:50px;color:#333;background:linear-gradient(#ffffff,#d9d9d9);border:2px solid #f2f2f2;box-shadow:0 3px 4px rgba(0,0,0,.35)}
.btn-plans{left:873px;top:309px;width:201px;height:52px;color:#3a2a00;background:linear-gradient(#fff38a,var(--yellow) 50%,var(--yellow-dark));border:2px solid #fff;box-shadow:0 3px 4px rgba(0,0,0,.35)}

.guides{position:absolute;left:0;top:568px;width:1123px;height:165px}
.guide-divider{position:absolute;left:556px;top:0;width:1px;height:165px;background:#e4e4e4}
.guide{position:absolute;top:0;width:480px;height:160px}
.guide-left{left:42px}
.guide-right{left:607px}
.guide-thumb{position:absolute;left:0;top:16px;width:198px;height:138px;border:1px solid #cfcfcf;background:#fff;padding:6px;box-shadow:0 8px 8px -6px rgba(0,0,0,.2)}
.guide-thumb span{display:block;width:100%;height:100%}
.thumb-relay{background:linear-gradient(#ececec,#dcdcdc)}
.thumb-kit{background:linear-gradient(#1a1a1a 0 52%,#ffffff 52%)}
.guide-title{position:absolute;left:220px;top:24px;width:260px;font-family:"Open Sans",sans-serif;font-size:15.5px;line-height:22px;color:var(--ink)}
.guide-right .guide-title{top:20px}
.btn-read{position:absolute;left:220px;top:111px;width:118px;height:38px;border-radius:19px;background:var(--btn-gray);color:#fff;font-family:"Open Sans",sans-serif;font-size:16px;display:flex;align-items:center;justify-content:center;box-shadow:0 2px 3px rgba(0,0,0,.35);text-decoration:none}

.about{position:absolute;left:0;top:810px;width:1123px;text-align:center}
.about::before{content:"";position:absolute;left:200px;top:0;width:690px;height:1px;background:linear-gradient(90deg,transparent,#e3e3e3,transparent)}
.about h2{padding-top:22px;font-family:"Open Sans",sans-serif;font-weight:400;font-size:28px;color:#333}
.about p{width:1000px;margin:20px auto 0;font-size:14.8px;line-height:21px;color:var(--text)}

.site-footer{position:absolute;left:0;top:1081px;width:1123px;height:119px;background:var(--footer);color:var(--footer-text);font-size:13px}
.footer-nav{position:absolute;left:45px;top:30px}
.footer-nav a{color:inherit;text-decoration:none}
.footer-nav .sep{margin:0 6px}
.copyright{position:absolute;left:46px;top:72px;font-size:12.5px}
.social{position:absolute;left:927px;top:32px;display:flex;gap:17px}
.social span{width:33px;height:33px;border-radius:50%;border:2px solid #9a9a9a}
</style>
</head>
<body>
<header class="site-header">
  <div class="brand">Posta.QZ</div>
  <nav class="main-nav"><a href="#">How it Work</a><span class="sep">|</span><a href="#">Support</a><span class="sep">|</span><a href="#">Login</a></nav>
</header>

<section class="hero">
  <div class="hero-photo" role="img" aria-label="Photo of a couple smiling at a laptop with email symbols floating beside them"></div>
  <ul class="hero-points">
    <li>We make Email Easy</li>
    <li>Give us five minute and we'll get you email from your domain.</li>
    <li>Easily forward mail from your custom domain name wherever you want it.</li>
    <li>You take the mail, we'll keep the spam.</li>
  </ul>
  <svg class="hero-arrow" width="64" height="70" viewBox="0 0 64 70" aria-hidden="true">
    <path d="M18 4 C4 20 8 46 40 52" fill="none" stroke="#f3c516" stroke-width="9" stroke-linecap="round"/>
    <path d="M36 38 L60 54 L34 64 Z" fill="#f3c516"/>
  </svg>
  <a class="btn btn-start" href="#">GET STARTED FREE</a>
  <a class="btn btn-plans" href="#">COMPARE PLANS</a>
</section>

<section class="guides">
  <article class="guide guide-left">
    <div class="guide-thumb"><span class="thumb-relay" role="img" aria-label="SkyRelay partner artwork"></span></div>
    <h3 class="guide-title">How to configure your SkyRelay DNS to use posta.qz</h3>
    <a class="btn-read" href="#">Read more</a>
  </article>
  <div class="guide-divider"></div>
  <article class="guide guide-right">
    <div class="guide-thumb"><span class="thumb-kit" role="img" aria-label="Screenshot of the DomainKit email login screen"></span></div>
    <h3 class="guide-title">Use posta.qz with your DomainKit domain registration for reliable email forwarding</h3>
    <a class="btn-read" href="#">Read more</a>
  </article>
</section>

<section class="about">
  <h2>About Us</h2>
  <p>We provide an easy way for people to manage email for a custom domain name. For example if you own "myfamilyword.example" you can point your DNS records to us and we'll make it easy to have emails addressed to your domain get forwarded to your existing email (vexmail, etc).</p>
  <p>(For technical folks, we have you point your dns mx records to us, hence the name. That way all your email hits us and we can redirect it wherever you want. We make it easy to manage a single domain or a bunch of domains</p>
</section>

<footer class="site-footer">
  <nav class="footer-nav"><a href="#">Home</a><span class="sep">|</span><a href="#">How it work</a><span class="sep">|</span><a href="#">Support</a><span class="sep">|</span><a href="#">Login</a><span class="sep">|</span><a href="#">Privacy Policy</a><span class="sep">|</span><a href="#">Contact</a></nav>
  <div class="copyright">Copyright 2014 posta.qz All Rights Reserved</div>
  <div class="social" aria-label="Social links"><span></span><span></span><span></span></div>
</footer>
</body>
</html>
```